Automotive debt collection business need several banners for new website

We are a debt recovery company called Quellton Recoveries Ltd who work specifically within the car automotive industry acting on behalf of our clients to recover debt which is owed to them. The advantage to using a company such as QRL is that it allows our clients the ability to outsource the work, removing the headache of dealing with the general public and reduces internal staff/overhead costs.
We collect various types of debt including:
Excess Mileage - this is charged when an individual has exceeded their permitted mileage allowance. This is calculated on a pence per mile basis on the mileage over the limit set when the contract was signed.
Damage - charged when a vehicle sustains more damage than is permitted within the contract. Damage could be dents to bodywork, large scratches, torn seats etc. Every area of damage over and above the allowed levels is detailed via a 'Damage Report' and a cost associated to that area of damage. The individual costs are then added up and a total charge formulated. The customer is liable to pay these charges as they have not cared for the vehicle in the appropriate manner whilst under their control
End of Contract Arrears - Once a contract ends and a vehicle is returned to our clients, there may be other charges that need to be repaid that remain outstanding.
We collect debt using a simple process. 1 - The customer is sent a letter as soon as the vehicle is collected advising them of the value of the debt. 2 - A few days later, we attempt to make contact via telephone or email. 3 - Once we contact the customer, we explain the debt and how the figure has been formulated (which is also explain in their letters). 4 - We negotiate (where appropriate) and agree a settlement figure. 5 - The customer pays the debt either in one installment over over a short payment plan.
Our new website (test URL only - http://testing.quelltonrecoveries.co.uk/) has a dual purpose. Firstly its to help promote our services to new clients who may be in the market for an alternative supplier (as far as we are aware, we are the only dedicated automotive debt collection company in the UK) and secondly, as a site to help those who owe money to pay and understand who we are (and that we are a registered, legal debt collection company)
Unlike other debt collection websites, we do not want generic images of people shaking hands, smiling etc. We want the images to be visually striking and make the website stand out from the competition. We are happy for these to be graphics rather than images.
We require some visual banners to represent what we do as a business and to emphasis that we specifically collect debt for the automotive sector.
These are websites that contain banners that we are NOT looking for:
http://uk.vabrix-partners.com/consumers/contact-data-working-hours/ - bland images of call centers/random people on phones etc
http://www.almsfield.com/client/
These are websites that contain banners that we class as OK:
http://www.norvanta.co.uk/business-services/debt-collection.html - fairly clear way of explaining their services
http://www.estatedues.co.uk/ - a slightly different slant using non-related images to explain what they can and cant do
http://www.pkwholdings.com/home/#.UhNNeD98CL0 - uses text to text banners to explain their offering
We require:
x4 - 870px X 500px - these will appear on the main homepage and rotate
x2 - 270px X 240px - static images that will to the right of the home page. One image needs to indicate some type of payment method as its a link to our online payment system, the second image refers to our other services (see the appropriate page on the website) these additional services include asset recovery, inspection, bespoke software solutions for the asset industry and auction disposal
x3 - 90px X 90px - Static images to represent payment methods that include cheque/card/bank transfer (see website for more info)
Our corporate colours are Black/Red/Grey
Depending on the designs received, we expect 2 rounds of modifications and we will advise those designers that have not been successful with positive feedback. We guarantee to pay the successful designer but work must be completed and ALL requested material produced and approved.

```html
<!DOCTYPE html>
<html lang="en">
<head>
<meta charset="utf-8">
<title>Quellton Recoveries – Five Star Support</title>
<link rel="stylesheet" href="https://fonts.googleapis.com/css2?family=Open+Sans:ital,wght@1,300;1,700;1,800&display=swap">
<style>
  :root {
    --red: #e3101b;
    --black: #111111;
    --sky-light: #f4f9fc;
    --sky: #dcebf4;
    --sky-deep: #b9d4e6;
    --silver-light: #dfe4e8;
    --silver: #a9b3bb;
    --silver-dark: #5f6a73;
    --white: #ffffff;
  }
  html, body {
    margin: 0;
    padding: 0;
    width: 1200px;
    height: 690px;
    overflow: hidden;
    background: var(--white);
  }
  .banner {
    position: relative;
    width: 1200px;
    height: 690px;
    overflow: hidden;
    font-family: "Open Sans", Arial, sans-serif;
    background: linear-gradient(160deg, var(--white) 0%, var(--sky-light) 35%, var(--sky) 70%, var(--sky-deep) 100%);
  }
  .backdrop-grid {
    position: absolute;
    right: 0;
    top: 0;
    width: 620px;
    height: 610px;
    background: radial-gradient(ellipse at 80% 35%, var(--sky-deep) 0%, var(--sky) 45%, rgba(220,235,244,0) 80%);
  }
  .vehicle-photo {
    position: absolute;
    left: 0;
    top: 0;
    width: 760px;
    height: 480px;
    border-bottom-right-radius: 60% 40%;
    background: linear-gradient(165deg, var(--silver-light) 0%, var(--silver) 45%, var(--silver-dark) 80%, var(--sky) 100%);
  }
  .swoosh {
    position: absolute;
    left: 0;
    top: 0;
  }
  .brand-mark {
    position: absolute;
    left: 880px;
    top: 330px;
    display: flex;
    align-items: center;
    gap: 14px;
    font-weight: 800;
    font-style: italic;
    font-size: 64px;
    color: var(--red);
    line-height: 1;
  }
  .brand-mark__square {
    width: 40px;
    height: 40px;
    background: var(--black);
  }
  .rule {
    position: absolute;
    left: 83px;
    width: 1041px;
  }
  .rule--black { top: 527px; height: 4px; background: var(--black); }
  .rule--red { top: 535px; height: 3px; background: var(--red); }
  .headline {
    position: absolute;
    right: 72px;
    top: 552px;
    margin: 0;
    font-size: 52px;
    font-style: italic;
    font-weight: 300;
    color: var(--black);
    letter-spacing: 0.5px;
    line-height: 1.1;
  }
  .headline strong { font-weight: 800; }
  .tagline {
    position: absolute;
    right: 72px;
    top: 617px;
    margin: 0;
    font-size: 35px;
    font-style: italic;
    font-weight: 700;
    color: var(--red);
    line-height: 1.1;
  }
</style>
</head>
<body>
  <div class="banner">
    <div class="backdrop-grid" role="img" aria-label="Soft light-blue perspective grid backdrop"></div>
    <div class="vehicle-photo" role="img" aria-label="Photograph of a silver saloon car, front three-quarter view, with a reflection beneath"></div>

    <svg class="swoosh" width="1200" height="690" viewBox="0 0 1200 690" aria-hidden="true">
      <path fill="var(--red)"
        d="M838 40
           C 905 140, 905 300, 810 390
           C 720 470, 560 505, 400 498
           C 250 490, 110 455, 0 405
           L 0 396
           C 120 440, 260 472, 400 478
           C 560 484, 700 450, 790 380
           C 880 300, 895 150, 838 40 Z"/>
    </svg>

    <div class="brand-mark">
      <span class="brand-mark__square"></span>
      <span class="brand-mark__name">QRL</span>
    </div>

    <div class="rule rule--black"></div>
    <div class="rule rule--red"></div>

    <h1 class="headline">FIVE STAR <strong>SUPPOR</strong></h1>
    <p class="tagline">Our trained advisors are here to help</p>
  </div>
</body>
</html>
```